Website for The Pendry Parlour

I require a website for "The Pendry Parlour" which is a blog type business for 40+ year old women covering books, true crime, history, travel and food. It needs to support blog posts, links to social media including YouTube videos, Instagram, TikTok and Facebook. The background theme needs to be like that of a newspaper. Easy to navigate and to allow me to post blogs/videos.

```html
<!DOCTYPE html>
<html lang="en">
<head>
<meta charset="utf-8">
<title>The Pendry Parlour</title>
<link rel="stylesheet" href="https://fonts.googleapis.com/css2?family=Oswald:wght@400;500;600&family=Poppins:wght@400;500;600&family=Playfair+Display:ital,wght@0,400;1,400&display=swap">
<style>
:root{
  --ink:#111111;
  --paper:#ffffff;
  --muted:#3a3a3a;
  --rule:#b5b5b5;
  --play:#e3262b;
}
*{box-sizing:border-box;margin:0;padding:0}
html,body{width:1200px;height:4967px;overflow:hidden;background:var(--paper);color:var(--ink)}
body{position:relative;font-family:'Poppins',sans-serif}
.block{position:absolute}
.heading{font-family:'Oswald',sans-serif;font-weight:600;text-transform:uppercase;line-height:1;letter-spacing:-.5px}
.serif-meta{font-family:'Playfair Display',serif;font-style:italic;font-size:12px;color:var(--muted)}
.photo{display:block}
.date{display:flex;align-items:center;gap:5px;font-size:12px;color:var(--ink)}
.date svg{width:11px;height:11px}
.card-title{font-family:'Oswald',sans-serif;font-weight:500;font-size:18px;line-height:1.25;white-space:nowrap}
.read-more{display:flex;align-items:center;gap:4px;font-size:11px;font-weight:600;letter-spacing:.3px}
.read-more svg{width:9px;height:9px}

/* header */
.logo{font-family:'Playfair Display',serif;font-weight:400;color:var(--ink);white-space:nowrap}
.site-logo{left:68px;top:34px;font-size:26px}
.main-nav{left:307px;top:31px;width:586px;height:44px;background:var(--ink);display:flex;align-items:center;padding-left:82px;gap:52px}
.main-nav a{color:var(--paper);text-decoration:none;font-size:14px;text-transform:uppercase}
.search{left:909px;top:31px;width:223px;height:46px;border:1.5px solid var(--ink);display:flex;align-items:center;justify-content:space-between;padding:0 14px 0 18px;font-size:13px}
.search svg{width:22px;height:22px}

/* hero */
.side-post{left:68px;width:200px}
.side-post .photo{width:200px;height:203px}
.side-post .date{margin-top:22px}
.side-post .card-title{font-size:17px;margin-top:8px;line-height:1.15;font-weight:400}
.side-post .card-title b{font-weight:600}
.author{font-size:11px;font-weight:600;font-style:italic;margin-top:8px}
.lead-card{left:289px;top:125px;width:623px;height:681px;border:1.5px solid var(--rule);padding:21px 21px 0}
.lead-card .photo{width:580px;height:385px}
.lead-title{font-family:'Oswald',sans-serif;font-size:26px;font-weight:400;line-height:1.15;margin-top:28px;white-space:nowrap}
.lead-title b{font-weight:600}
.lead-text{font-size:15px;line-height:1.7;margin-top:20px}
.lead-rule{width:30px;height:2px;background:var(--ink);margin-top:14px}
.lead-author{font-size:15px;font-weight:500;margin-top:10px}
.lead-time{font-size:13px;font-style:italic;color:var(--muted)}
.latest{left:932px;top:128px;width:200px}
.latest-head{display:flex;justify-content:space-between;align-items:center;border-bottom:2px solid var(--ink);padding-bottom:3px}
.latest-head h3{font-family:'Oswald',sans-serif;font-size:15px;font-weight:600}
.mini-arrows{display:flex;gap:3px}
.mini-arrows span{width:13px;height:13px;border:1px solid var(--ink);display:flex;align-items:center;justify-content:center}
.mini-arrows svg{width:7px;height:7px}
.latest-item{display:flex;gap:12px;align-items:center;height:135px;border-bottom:1px solid #ddd}
.latest-item:first-of-type{margin-top:10px}
.latest-item .photo{width:90px;height:90px;border-radius:50%;border:3px solid var(--ink);flex:none}
.latest-item p{font-family:'Oswald',sans-serif;font-size:16px;line-height:1.2}

/* divider */
.divider{left:68px;width:1064px;height:14px}
.divider::before{content:"";position:absolute;left:0;right:0;top:4px;height:4px;background:var(--ink)}
.divider::after{content:"";position:absolute;left:0;right:0;top:11px;height:1px;background:var(--ink)}
.divider span{position:absolute;left:525px;top:-2px;width:14px;height:14px;background:var(--ink);transform:rotate(45deg);z-index:1}

/* section head */
.section-title{left:68px;font-size:54px}
.arrows{display:flex;gap:9px}
.arrows span{width:25px;height:25px;border:1.5px solid var(--ink);border-radius:3px;display:flex;align-items:center;justify-content:center;background:var(--paper)}
.arrows svg{width:10px;height:10px}
.section-arrows{left:1074px}

/* books */
.book-row{left:68px;top:1138px;width:1064px;display:flex;gap:31px}
.book{width:243px}
.book .photo{height:189px}
.book .date{margin-top:20px}
.book .card-title{margin-top:12px}
.book .read-more{margin-top:10px}

/* crime */
.crime-row{left:66px;top:1761px;width:1070px;display:flex;gap:26px}
.crime{width:248px;height:372px;border:1.5px solid var(--rule);padding:2px 2px 0}
.crime .photo{height:188px}
.crime .body{padding:0 18px}
.crime .date{margin-top:22px}
.crime .card-title{margin-top:8px;font-size:17.5px}
.crime .excerpt{font-size:13px;line-height:1.5;margin-top:6px}
.crime .read-more{margin-top:16px}

/* history */
.feature{left:68px;top:2496px;width:520px}
.feature .photo{height:440px}
.feature h3{font-family:'Oswald',sans-serif;font-weight:600;font-size:25px;line-height:1.25;margin-top:40px;white-space:nowrap}
.feature p{font-size:13px;line-height:1.5;margin-top:14px}
.byline{display:flex;align-items:center;gap:10px;margin-top:30px;font-size:15px;font-weight:500}
.byline i{font-family:'Playfair Display',serif;font-size:13px;font-weight:400}
.byline .sep{width:1px;height:14px;background:var(--ink)}
.byline .date{font-family:'Playfair Display',serif;font-size:11px}
.history-grid{left:637px;top:2498px;width:486px;display:grid;grid-template-columns:226px 226px;column-gap:34px;row-gap:40px}
.history-grid .photo{height:202px}
.history-grid p{font-family:'Oswald',sans-serif;font-size:17px;font-weight:400;line-height:1.5;margin-top:20px;white-space:nowrap}
.history-grid .serif-meta{margin-top:6px;font-size:13px}

/* travel */
.travel-title{left:58px;top:3380px;font-size:54px}
.video-board{left:64px;top:3492px;width:1068px}
.video-top{display:flex;height:341px}
.video-lead{width:534px;background:var(--ink);color:var(--paper);padding:40px 24px 0}
.video-tag{font-family:'Oswald',sans-serif;font-size:18px;text-transform:uppercase}
.video-lead h3{font-family:'Oswald',sans-serif;font-weight:600;font-size:24px;line-height:1.25;margin-top:28px;white-space:nowrap}
.video-lead p{font-size:12px;line-height:1.7;margin-top:18px}
.video-lead .ago{font-family:'Playfair Display',serif;font-style:italic;font-size:14px;margin-top:20px}
.video-media{position:relative;flex:1}
.video-media .photo{position:absolute;inset:0}
.play{position:absolute;border-radius:50%;background:var(--play);display:flex;align-items:center;justify-content:center}
.play svg{width:40%;height:40%}
.video-bottom{display:flex;gap:6px;margin-top:4px;height:175px}
.video-card{flex:1;display:flex;background:var(--ink);color:var(--paper)}
.video-card .media{position:relative;width:266px;height:100%;flex:none}
.video-card .media .photo{position:absolute;inset:0}
.video-card .text{padding:30px 18px 0 32px}
.video-card .video-tag{font-size:15px}
.video-card h4{font-family:'Oswald',sans-serif;font-weight:600;font-size:16px;line-height:1.2;margin-top:18px;white-space:nowrap}
.video-card .date{color:var(--paper);font-family:'Playfair Display',serif;font-style:italic;font-size:10px;margin-top:10px}
.video-card .date svg{color:var(--paper)}
.video-card .by{font-family:'Playfair Display',serif;font-size:11px;margin-top:6px}
.board-arrow{top:3908px}

/* newsletter */
.newsletter{left:0;top:4185px;width:1200px;text-align:center}
.newsletter h2{font-size:52px}
.newsletter p{font-size:12px;line-height:1.7;width:760px;margin:22px auto 0}
.signup{left:266px;top:4348px;width:668px;height:66px;border:1.5px solid #999;display:flex;align-items:center;padding:0 8px 0 18px;justify-content:space-between}
.signup span{font-size:13px}
.signup button{width:135px;height:50px;background:var(--ink);color:var(--paper);border:0;font-family:'Poppins',sans-serif;font-weight:500;font-size:13px;text-transform:uppercase}

/* footer */
.footer-logo{left:0;top:4575px;width:1200px;text-align:center;font-size:44px}
.socials{left:525px;top:4655px;display:flex;gap:6px}
.socials span{width:34px;height:34px;border:2px solid var(--ink);border-radius:50%}
.site-footer{left:0;top:4745px;width:1200px;height:222px;background:#000;color:var(--paper)}
.contacts{position:absolute;top:60px;left:245px;display:flex;align-items:center;font-size:13px;line-height:1.3}
.contact{display:flex;align-items:center;gap:14px}
.contact .ico{width:32px;height:32px;border-radius:50%;background:var(--paper);display:flex;align-items:center;justify-content:center}
.contact .ico svg{width:17px;height:17px}
.footer-rule{position:absolute;left:68px;top:139px;width:1064px;height:1px;background:#777}
.copyright{position:absolute;top:166px;width:100%;text-align:center;font-size:12px}
</style>
</head>
<body>

<svg width="0" height="0" style="position:absolute">
  <defs>
    <symbol id="cal" viewBox="0 0 12 12"><rect x="1" y="2" width="10" height="9" fill="currentColor"/><rect x="2.5" y="5" width="7" height="4.5" fill="#fff"/><rect x="3" y="0.5" width="1.2" height="2.5" fill="currentColor"/><rect x="7.8" y="0.5" width="1.2" height="2.5" fill="currentColor"/></symbol>
    <symbol id="out" viewBox="0 0 10 10"><path d="M2 8L8 2M3.5 2H8V6.5" fill="none" stroke="currentColor" stroke-width="1.4"/></symbol>
    <symbol id="prev" viewBox="0 0 10 10"><path d="M6.5 1.5L3 5l3.5 3.5" fill="none" stroke="currentColor" stroke-width="1.4"/></symbol>
    <symbol id="next" viewBox="0 0 10 10"><path d="M3.5 1.5L7 5 3.5 8.5" fill="none" stroke="currentColor" stroke-width="1.4"/></symbol>
    <symbol id="tri" viewBox="0 0 10 10"><path d="M3 1.5L9 5 3 8.5z" fill="#fff"/></symbol>
  </defs>
</svg>

<!-- header -->
<div class="block logo site-logo">The Pendry Parlour</div>
<nav class="block main-nav"><a>Home</a><a>About Us</a><a>Blog</a><a>Contact Us</a></nav>
<div class="block search"><span>SEARCH</span><svg viewBox="0 0 24 24"><circle cx="10" cy="10" r="7" fill="none" stroke="#111" stroke-width="1.8"/><path d="M15 15l6 6" stroke="#111" stroke-width="1.8"/></svg></div>

<!-- hero -->
<article class="block side-post" style="top:125px">
  <div class="photo" role="img" aria-label="Old parchment scrolls and an inkwell on a desk" style="background:linear-gradient(135deg,#5a4530,#b8996c 50%,#6a5238)"></div>
  <div class="date"><svg><use href="#cal"/></svg>01 August 2025</div>
  <h3 class="card-title"><b>History</b>/ Lorem ipsum dolor<br>sit amet, consectetur adi</h3>
  <p class="author">Harriet Vale</p>
</article>
<article class="block side-post" style="top:478px">
  <div class="photo" role="img" aria-label="Street vendor carrying baskets in a market" style="background:linear-gradient(160deg,#6e7a8c,#3b4d6a 50%,#5a5450)"></div>
  <div class="date"><svg><use href="#cal"/></svg>01 August 2025</div>
  <h3 class="card-title"><b>History</b>/ Lorem ipsum dolor<br>sit amet, consectetur adi</h3>
  <p class="author">Harriet Vale</p>
</article>

<article class="block lead-card">
  <div class="photo" role="img" aria-label="Elderly man reading a newspaper by a sunlit window" style="background:radial-gradient(circle at 75% 30%,#e2b979,#8a6238 40%,#2e2118 80%)"></div>
  <h2 class="lead-title"><b>CRIME</b> /Lorem ipsum dolor sit amet, consectetur<br>adipiscing elit, sed do eiusmod tempor incid</h2>
  <p class="lead-text">Lorem ipsum dolor sit amet, consectetur adipiscing elit, sed do eiusm od tempor incididunt ut labore et dolore magna aliqua. Quis ipsum suspend ultrices gravida...</p>
  <div class="lead-rule"></div>
  <p class="lead-author">Harriet Vale</p>
  <p class="lead-time">4 days ago</p>
</article>

<aside class="block latest">
  <div class="latest-head"><h3>LATEST POSTS</h3><div class="mini-arrows"><span><svg><use href="#prev"/></svg></span><span><svg><use href="#next"/></svg></span></div></div>
  <div class="latest-item"><div class="photo" role="img" aria-label="Reader with newspaper" style="background:radial-gradient(circle,#b98a57,#3a2c20)"></div><div><p>Lorem ipsum<br>dolor sit amet,<br>consectetur</p><span class="serif-meta">2 days ago</span></div></div>
  <div class="latest-item"><div class="photo" role="img" aria-label="Red market stall" style="background:radial-gradient(circle,#d23a33,#5a1a18)"></div><div><p>Lorem ipsum<br>dolor sit amet,<br>consectetur</p><span class="serif-meta">2 days ago</span></div></div>
  <div class="latest-item"><div class="photo" role="img" aria-label="Reader with newspaper" style="background:radial-gradient(circle,#b98a57,#3a2c20)"></div><div><p>Lorem ipsum<br>dolor sit amet,<br>consectetur</p><span class="serif-meta">2 days ago</span></div></div>
  <div class="latest-item"><div class="photo" role="img" aria-label="Street market scene" style="background:radial-gradient(circle,#5b6a88,#2b3344)"></div><div><p>Lorem ipsum<br>dolor sit amet,<br>consectetur</p><span class="serif-meta">2 days ago</span></div></div>
  <div class="latest-item" style="border-bottom:0"><div class="photo" role="img" aria-label="Street market scene" style="background:radial-gradient(circle,#5b6a88,#2b3344)"></div><div><p>Lorem ipsum<br>dolor sit amet,<br>consectetur</p><span class="serif-meta">2 days ago</span></div></div>
</aside>

<div class="block divider" style="top:882px"><span></span></div>

<!-- books -->
<h2 class="block heading section-title" style="top:1012px">Books</h2>
<div class="block arrows section-arrows" style="top:1025px"><span><svg><use href="#prev"/></svg></span><span><svg><use href="#next"/></svg></span></div>
<div class="block book-row">
  <article class="book"><div class="photo" role="img" aria-label="Open book on a table" style="background:linear-gradient(160deg,#cfc7bc,#8d7e6c 60%,#d8d1c6)"></div><div class="date"><svg><use href="#cal"/></svg>18 July 2025</div><h3 class="card-title">Lorem ipsum dolor sit ame<br>etcons ectetur adipiscing</h3><div class="read-more">READ MORE <svg><use href="#out"/></svg></div></article>
  <article class="book"><div class="photo" role="img" aria-label="Reading glasses on a stack of books" style="background:linear-gradient(160deg,#efefef,#8a8a8a 60%,#5c5c5c)"></div><div class="date"><svg><use href="#cal"/></svg>22 January 2025</div><h3 class="card-title">Lorem ipsum dolor sit ame<br>etcons ectetur adipiscing</h3><div class="read-more">READ MORE <svg><use href="#out"/></svg></div></article>
  <article class="book"><div class="photo" role="img" aria-label="Shelves of stacked books" style="background:linear-gradient(160deg,#707070,#c7c7c7 50%,#3e3e3e)"></div><div class="date"><svg><use href="#cal"/></svg>18 July 2025</div><h3 class="card-title">Lorem ipsum dolor sit ame<br>etcons ectetur adipiscing</h3><div class="read-more">READ MORE <svg><use href="#out"/></svg></div></article>
  <article class="book"><div class="photo" role="img" aria-label="Old books stacked in snow" style="background:linear-gradient(160deg,#4b4b4b,#9a9a9a 55%,#e9e9e9)"></div><div class="date"><svg><use href="#cal"/></svg>22 January 2025</div><h3 class="card-title">Lorem ipsum dolor sit ame<br>etcons ectetur adipiscing</h3><div class="read-more">READ MORE <svg><use href="#out"/></svg></div></article>
</div>

<div class="block divider" style="top:1530px"><span></span></div>

<!-- true crime -->
<h2 class="block heading section-title" style="top:1637px">True Crime</h2>
<div class="block arrows section-arrows" style="top:1650px"><span><svg><use href="#prev"/></svg></span><span><svg><use href="#next"/></svg></span></div>
<div class="block crime-row">
  <article class="crime"><div class="photo" role="img" aria-label="Shadowy figure in a dark alley" style="background:linear-gradient(160deg,#4a4a48,#1e1e1e)"></div><div class="body"><div class="date"><svg><use href="#cal"/></svg>18 July 2025</div><h3 class="card-title">Lorem ipsum dolor sit ame<br>etcons ectetur adipiscing</h3><p class="excerpt">Lorem ipsum dolor sit amet cons ectetur adipiscing</p><div class="read-more">READ MORE <svg><use href="#out"/></svg></div></div></article>
  <article class="crime"><div class="photo" role="img" aria-label="Police officers at a taped-off scene" style="background:linear-gradient(160deg,#5a2a8a,#2a2f7a 50%,#a3305a)"></div><div class="body"><div class="date"><svg><use href="#cal"/></svg>18 July 2025</div><h3 class="card-title">Lorem ipsum dolor sit ame<br>etcons ectetur adipiscing elit,</h3><p class="excerpt">Lorem ipsum dolor sit amet cons ectetur adipiscing</p><div class="read-more">READ MORE <svg><use href="#out"/></svg></div></div></article>
  <article class="crime"><div class="photo" role="img" aria-label="Frightened woman held by an attacker" style="background:linear-gradient(160deg,#3a3431,#9b8070 55%,#2c2826)"></div><div class="body"><div class="date"><svg><use href="#cal"/></svg>18 July 2025</div><h3 class="card-title">Lorem ipsum dolor sit ame<br>etcons ectetur adipiscing elit,</h3><p class="excerpt">Lorem ipsum dolor sit amet cons ectetur adipiscing</p><div class="read-more">READ MORE <svg><use href="#out"/></svg></div></div></article>
  <article class="crime"><div class="photo" role="img" aria-label="Police officer seen from behind at a protest" style="background:linear-gradient(160deg,#8a8c90,#3a3f48 55%,#1d2128)"></div><div class="body"><div class="date"><svg><use href="#cal"/></svg>18 July 2025</div><h3 class="card-title">Lorem ipsum dolor sit ame<br>etcons ectetur adipiscing elit,</h3><p class="excerpt">Lorem ipsum dolor sit amet cons ectetur adipiscing</p><div class="read-more">READ MORE <svg><use href="#out"/></svg></div></div></article>
</div>

<div class="block divider" style="top:2260px"><span></span></div>

<!-- history -->
<h2 class="block heading section-title" style="top:2390px">History</h2>
<div class="block arrows section-arrows" style="top:2404px"><span><svg><use href="#prev"/></svg></span><span><svg><use href="#next"/></svg></span></div>
<article class="block feature">
  <div class="photo" role="img" aria-label="Rows of ancient terracotta warrior statues" style="background:linear-gradient(150deg,#6f6d69,#b3b0aa 45%,#4f4d4a)"></div>
  <h3>Lorem ipsum dolor sit ame etcons ectetur adipiscing<br>elit, sed doeius mod tempor incididunt ut labore</h3>
  <p>Lorem ipsum dolor sit amet, consectetur adipiscing elit, sed do eiusmod tempor incididunt ut labore et dolore magna aliqua. Quis ipsum susp endisse ultrices gravida. Risus commodo viverra maecenas accumsan lacus vel facilisis.</p>
  <div class="byline"><i>by</i> Harriet Vale <span class="sep"></span><span class="date"><svg><use href="#cal"/></svg>18 July 2025</span></div>
</article>
<div class="block history-grid">
  <article><div class="photo" role="img" aria-label="Camel caravan in a desert town" style="background:linear-gradient(170deg,#7f93b0,#b08a5e 60%,#7a5a3a)"></div><p>Lorem ipsum dolor sit amet, cons<br>ectetur adipiscing elit, sed do</p><div class="serif-meta">2 days ago</div></article>
  <article><div class="photo" role="img" aria-label="Antique bellows camera" style="background:radial-gradient(circle at 55% 50%,#c08a4a,#5a3a1e 60%,#1e140c)"></div><p>Lorem ipsum dolor sit amet, cons<br>ectetur adipiscing elit, sed do</p><div class="serif-meta">2 days ago</div></article>
  <article><div class="photo" role="img" aria-label="Knight in armour against a starry sky" style="background:radial-gradient(circle at 50% 45%,#c6649a,#4a2a7a 55%,#150f2a)"></div><p>Lorem ipsum dolor sit amet, cons<br>ectetur adipiscing elit, sed do</p><div class="serif-meta">2 days ago</div></article>
  <article><div class="photo" role="img" aria-label="Carved mountain monument under blue sky" style="background:linear-gradient(180deg,#3b6bb0,#d08a4a 55%,#7a4a22)"></div><p>Lorem ipsum dolor sit amet, cons<br>ectetur adipiscing elit, sed do</p><div class="serif-meta">2 days ago</div></article>
</div>

<div class="block divider" style="top:3268px"><span></span></div>

<!-- travel and food -->
<h2 class="block heading travel-title">Travel and Food</h2>
<div class="block arrows board-arrow" style="left:18px"><span><svg><use href="#prev"/></svg></span></div>
<div class="block arrows board-arrow" style="left:1146px"><span><svg><use href="#next"/></svg></span></div>
<section class="block video-board">
  <div class="video-top">
    <div class="video-lead">
      <div class="video-tag">Videos</div>
      <h3>Lorem ipsum dolor sit amet, consectetur adipis<br>cing elit, sed do eiusmod tempor incididunt ut</h3>
      <p>Lorem ipsum dolor sit amet, consectetur adipiscing elit, sed do eiusmod tempor incididunt ut labore et dolore magna aliqua. Quis ipsum susp endisse ultrices gravida. Risus commodo viverra ecenas accumsan lacus vel facilisis.....</p>
      <div class="ago">5 days ago</div>
    </div>
    <div class="video-media">
      <div class="photo" role="img" aria-label="City skyline with a cyclist on a riverside road" style="background:linear-gradient(180deg,#a9b7c4,#6c7c8c 50%,#3e4a44 80%,#5a5a52)"></div>
      <span class="play" style="left:260px;top:130px;width:50px;height:50px"><svg><use href="#tri"/></svg></span>
    </div>
  </div>
  <div class="video-bottom">
    <article class="video-card">
      <div class="media"><div class="photo" role="img" aria-label="Historic street lit at dusk" style="background:linear-gradient(170deg,#2a3d6a,#6a6a7a 55%,#c99a5a)"></div><span class="play" style="left:116px;top:68px;width:34px;height:34px"><svg><use href="#tri"/></svg></span></div>
      <div class="text"><div class="video-tag">Videos</div><h4>Lorem ipsum dolor sit amet,<br>consectetur adipis</h4><div class="date"><svg><use href="#cal"/></svg>January 07, 2025</div><div class="by">Harriet Vale</div></div>
    </article>
    <article class="video-card">
      <div class="media"><div class="photo" role="img" aria-label="Travellers silhouetted in an airport terminal" style="background:linear-gradient(180deg,#2a2a2a,#b9c2c8 45%,#6a6e72)"></div><span class="play" style="left:116px;top:68px;width:34px;height:34px"><svg><use href="#tri"/></svg></span></div>
      <div class="text"><div class="video-tag">Videos</div><h4>Lorem ipsum dolor sit amet,<br>consectetur adipis</h4><div class="date"><svg><use href="#cal"/></svg>January 07, 2025</div><div class="by">Harriet Vale</div></div>
    </article>
  </div>
</section>

<div class="block divider" style="top:4115px"><span></span></div>

<!-- newsletter -->
<section class="block newsletter">
  <h2 class="heading">Newsletter Sign Up</h2>
  <p>Lorem ipsum dolor sit amet, consectetur adipiscing elit, sed do eiusmod tempor incididunt ut labore et dolore magna aliqua. Quis ipsum suspendisse ultrices gravida. Risus commodo viverra maecenas accumsan lacus vel</p>
</section>
<form class="block signup"><span>Enter Your Email Address</span><button type="button">Subscribe</button></form>

<div class="block divider" style="top:4499px"><span></span></div>

<!-- footer -->
<div class="block logo footer-logo">The Pendry Parlour</div>
<div class="block socials">
  <span aria-label="Video channel"></span><span aria-label="Community page"></span><span aria-label="Photo feed"></span><span aria-label="Short clips"></span>
</div>
<footer class="block site-footer">
  <div class="contacts">
    <div class="contact"><span class="ico"><svg viewBox="0 0 20 20"><path d="M5 2l3 3-2 2.5c1 2.2 2.6 3.8 4.8 4.8L13.3 10l3 3-2.2 3C8.5 15.5 4.5 11.5 3 5z" fill="#000"/></svg></span><div>CALL US<br>020 555 0148</div></div>
    <div class="contact" style="margin-left:70px"><span class="ico"><svg viewBox="0 0 20 20"><rect x="2" y="4" width="16" height="12" rx="1.5" fill="#000"/><path d="M3 5l7 6 7-6" fill="none" stroke="#fff" stroke-width="1.4"/></svg></span><div>EMAIL US<br>hello@pendryparlour.example</div></div>
    <div class="contact" style="margin-left:90px"><span class="ico"><svg viewBox="0 0 20 20"><path d="M10 1.5a6 6 0 016 6c0 4.5-6 11-6 11s-6-6.5-6-11a6 6 0 016-6z" fill="#000"/><circle cx="10" cy="7.5" r="2.2" fill="#fff"/></svg></span><div>Address line Dummy Here<br>Address line Here</div></div>
  </div>
  <div class="footer-rule"></div>
  <p class="copyright">Copyright © 2025 All Rights Reserved By The Pendry Parlour</p>
</footer>

</body>
</html>
```